Web Design - Personal Item Tags Portal

web page designs need to be created for a new company that provides item tracking tags and lets users register and report stolen/found items.
The theme of the designs needs to be energetic and convey a sense of freedom and adventure - where the user does not have to worry about their items since they have all been "tagged".
the client likes parts of the site at: http://www.plimcraft.example/
they like:
1. slider images at top of pages. large slider on front page. fixed smaller height picture on internal pages
2. fixed company message on left-hand-side
3. My Account button to be clear and stand out

other comments:
clean, simple
• brand focused
• will have clear call to actions
• will include a description of what and why
• will appeal to both males and females

sections that the website will have are:
Home
About Us
How it works
Why
Case Studies
Uses and Applications
Shop
Contact Us

please create 2 designs : 1 home page, 1 internal page

Final winner will also require HTML slicing to be done.

hi, i have now updated the images so they work. sorry!

Hi, looking at all the designs that are coming in, alot of them are great. Designers need to remember to make the register for an account button more prominent. Also, there should be a "report found" and "report lost" buttons on the front-page and should be prominent as well.

Thanks

Hi, the customer has come back with a few comments and modifications for the designs, if you are able to make some tweaks to your submissions, that will be great:

The client would like the designs to be modified to highlight 3 main actions:
1. Log In/Register
2. Find an Owner
3. Lost an Item

The home page shouldnt be too content heavy in terms of text, it should only have major highlight points of what the system does (the 3 points listed above). the inner page designs are OK to have more text though.

i will also upload some notes from the customer that can be used as a guide and also include the design styles which the customer likes (but is not entirely happy with).

uploaded image files (3) with customer feedback comments

```html
<!DOCTYPE html>
<html lang="en">
<head>
<meta charset="utf-8">
<title>Roamlet — adventure first</title>
<link rel="stylesheet" href="https://fonts.googleapis.com/css2?family=PT+Sans:wght@400;700&family=Roboto+Condensed:wght@400&family=Exo+2:wght@300;400&display=swap">
<style>
  :root{
    --header-bg:#1a1513;
    --header-line:#1f7fc4;
    --accent:#4aa8ea;
    --cyan:#18b4ee;
    --band-top:#2aa6df;
    --band-bottom:#0f86c4;
    --btn-top:#2ab0e6;
    --btn-bottom:#0d7fbf;
    --text:#141414;
    --nav-text:#e8e8e8;
    --message-bg:#cfe5f8;
    --footer-bg:#f6f6f6;
    --muted:#6a6a6a;
  }
  *{box-sizing:border-box;margin:0;padding:0}
  html,body{width:1200px;height:900px;overflow:hidden;background:#fff}
  body{position:relative;font-family:"PT Sans",sans-serif;color:var(--text)}

  .site-header{position:absolute;left:0;top:0;width:1200px;height:150px;background:var(--header-bg)}
  .header-rule{position:absolute;left:188px;top:107px;width:1012px;height:1px;background:var(--header-line)}
  .brand-burst{position:absolute;left:0;top:0;width:188px;height:150px;
    background:radial-gradient(circle at 80px 80px,#dff3ff 0,#4ab4ee 22px,#1566b0 60px,#0b2746 110px,var(--header-bg) 150px)}
  .brand-name{position:absolute;left:250px;top:6px;font-size:48px;font-weight:700;color:#fff;letter-spacing:1px}
  .brand-tagline{position:absolute;left:255px;top:70px;font-family:"Roboto Condensed",sans-serif;font-size:22px;color:#fff}

  .register-btn{position:absolute;left:862px;top:38px;width:272px;height:42px;border-radius:4px;
    background:linear-gradient(var(--btn-top),var(--btn-bottom));border:1px solid #5cc8f2;
    color:#fff;font-size:15px;text-align:center;line-height:40px;text-decoration:none}
  .register-btn strong{font-size:20px}

  .main-nav{position:absolute;top:121px;left:0;width:1200px;font-size:12px}
  .main-nav a{position:absolute;color:var(--nav-text);text-decoration:none;white-space:nowrap}
  .main-nav a.is-current{color:var(--accent)}

  .action-band{position:absolute;left:0;top:150px;width:1200px;height:72px;
    background:repeating-linear-gradient(0deg,rgba(255,255,255,.07) 0 2px,transparent 2px 5px),linear-gradient(var(--band-top),var(--band-bottom))}
  .report-btn{position:absolute;top:16px;width:231px;height:40px;border-radius:4px;background:#050505;
    border:1px solid #7a7a7a;color:#fff;font-size:18px;line-height:38px;text-decoration:none;overflow:hidden}
  .report-btn .radar{position:absolute;left:0;top:0;width:62px;height:38px;
    background:radial-gradient(circle at 30px 19px,#4fc26a 0,#1d6b2c 14px,#0b2b12 26px,#050505 40px)}
  .report-btn span{position:absolute;left:62px;right:0;text-align:center}

  .intro{position:absolute;left:179px;top:274px;width:340px}
  .intro h1{font-size:32px;font-weight:400;color:var(--accent);line-height:1;white-space:nowrap}
  .intro p{font-size:17px;line-height:19.6px;margin-top:3px}
  .learn-btn{position:absolute;left:181px;top:414px;width:137px;height:28px;border-radius:3px;
    background:linear-gradient(var(--btn-top),var(--btn-bottom));border:1px solid #5cc8f2;
    color:#fff;font-size:15px;line-height:26px;text-align:center;text-decoration:none}

  .slide{position:absolute;background:#000;overflow:hidden;border:1px solid #555}
  .slide .scene{position:absolute;left:0;top:0;height:100%;
    background:linear-gradient(180deg,#2a5f9a,#5aa0e0)}
  .slide .caption{position:absolute;font-family:"Exo 2",sans-serif;color:var(--cyan);text-align:right;line-height:1;white-space:nowrap}
  .slide-main{left:583px;top:274px;width:468px;height:332px}
  .slide-main .scene{width:150px}
  .slide-main .caption{right:12px;top:153px}
  .slide-main .caption b{display:block;font-weight:400;font-size:35px}
  .slide-main .caption i{display:block;font-style:normal;font-size:19px;margin-top:2px;margin-right:10px}
  .slide-thumb{top:486px;width:171px;height:121px}
  .slide-thumb .scene{width:56px}
  .slide-thumb .caption{right:4px;top:56px}
  .slide-thumb .caption b{display:block;font-weight:400;font-size:13px}
  .slide-thumb .caption i{display:block;font-style:normal;font-size:7px;margin-right:4px}

  .message-band{position:absolute;left:0;top:662px;width:1200px;height:104px;background:var(--message-bg);
    text-align:center;font-size:17px;line-height:21px;padding-top:17px}

  .site-footer{position:absolute;left:0;top:766px;width:1200px;height:134px;background:var(--footer-bg)}
  .footer-col{position:absolute;top:23px;font-size:12px;line-height:22px;list-style:none}
  .footer-col a{color:var(--text);text-decoration:none}
  .follow{position:absolute;left:878px;top:26px;width:180px}
  .follow h2{font-size:17px;font-weight:400;color:var(--muted)}
  .social{list-style:none;display:flex;flex-wrap:wrap;gap:4px 10px;margin-top:8px;font-size:11px}
  .social li{display:flex;align-items:center;gap:4px}
  .social i{display:inline-block;width:9px;height:9px}
</style>
</head>
<body>
  <header class="site-header">
    <div class="brand-burst" role="img" aria-label="Blue light burst behind the brand emblem"></div>
    <div class="header-rule"></div>
    <div class="brand-name">Roamlet</div>
    <div class="brand-tagline">. . . adventure first</div>
    <a class="register-btn" href="#">REGISTER FOR A <strong>FREE</strong> ACCOUNT</a>
    <nav class="main-nav">
      <a class="is-current" href="#" style="left:569px">Home</a>
      <a href="#" style="left:623px">About Us</a>
      <a href="#" style="left:690px">How it works</a>
      <a href="#" style="left:776px">Why</a>
      <a href="#" style="left:820px">Case Studies</a>
      <a href="#" style="left:903px">Uses and Applications</a>
      <a href="#" style="left:1034px">Shop</a>
      <a href="#" style="left:1081px">Contact Us</a>
    </nav>
  </header>

  <section class="action-band">
    <a class="report-btn" href="#" style="left:313px"><i class="radar" role="img" aria-label="Green radar screen"></i><span>REPORT FOUND</span></a>
    <a class="report-btn" href="#" style="left:688px"><i class="radar" role="img" aria-label="Green radar screen"></i><span>REPORT LOST</span></a>
  </section>

  <section class="intro">
    <h1>Lorem ipsum dolor sit</h1>
    <p>Consectetur adipisicing elit, sed do eiusmod tempor incididunt ut labore et dolore magna aliqua. Ut enim ad minim veniam, quis nostrud exercitation ullamco laboris nisi ut a</p>
  </section>
  <a class="learn-btn" href="#">LEARN MORE</a>

  <div class="slide slide-thumb" style="left:179px">
    <div class="scene" role="img" aria-label="Climber silhouetted on a dark overhang against blue sky"></div>
    <div class="caption"><b>‘Adventure First’</b><i>Intrepid Trail Solutions</i></div>
  </div>
  <div class="slide slide-thumb" style="left:374px">
    <div class="scene" role="img" aria-label="Climber silhouetted on a dark overhang against blue sky"></div>
    <div class="caption"><b>‘Adventure First’</b><i>Intrepid Trail Solutions</i></div>
  </div>
  <div class="slide slide-main">
    <div class="scene" role="img" aria-label="Rock climber hanging from a dark cliff overhang against a blue sky"></div>
    <div class="caption"><b>‘Adventure First’</b><i>Intrepid Trail Solutions</i></div>
  </div>

  <section class="message-band">
    <p>Lorem ipsum dolor sit</p>
    <p>Consectetur adipisicing elit, sed do eiusmod tempor incididunt ut labore et dolore magna aliqua.</p>
    <p>Ut enim ad minim veniam, quis nostrud exercitation ullamco laboris nisi ut a</p>
  </section>

  <footer class="site-footer">
    <ul class="footer-col" style="left:179px"><li><a href="#">Lorem ipsum</a></li><li><a href="#">Lorem ipsum</a></li><li><a href="#">Lorem ipsum</a></li></ul>
    <ul class="footer-col" style="left:306px"><li><a href="#">Lorem ipsum</a></li><li><a href="#">Lorem ipsum</a></li><li><a href="#">Lorem ipsum</a></li></ul>
    <ul class="footer-col" style="left:432px"><li><a href="#">Lorem ipsum</a></li><li><a href="#">Lorem ipsum</a></li><li><a href="#">Lorem ipsum</a></li></ul>
    <ul class="footer-col" style="left:558px"><li><a href="#">Lorem ipsum</a></li><li><a href="#">Lorem ipsum</a></li><li><a href="#">Lorem ipsum</a></li></ul>
    <ul class="footer-col" style="left:685px"><li><a href="#">Lorem ipsum</a></li><li><a href="#">Lorem ipsum</a></li><li><a href="#">Lorem ipsum</a></li></ul>
    <div class="follow">
      <h2>Follow Us</h2>
      <ul class="social">
        <li><i style="background:#d9432f"></i>Plazo</li>
        <li><i style="background:#d9432f"></i>Clipcast</li>
        <li><i style="background:#3b5d9c"></i>Friendly</li>
        <li><i style="background:#35a9df"></i>Chirpa</li>
        <li><i style="background:#d83a3a"></i>Email</li>
      </ul>
    </div>
  </footer>
</body>
</html>
```